Business card and stationery concept for weight management and nutrition practice
trueLeaf Guidance
Dear Designers,
I have uploaded my logo files and am looking forward to everyone's designs.
I would like to see designs that do not feature my logo quite so prominently - that is, the logo does not have to be very large.
Also, instead of bold abstract curves and shapes I'd like to see accents that are more feminine.
Thanks everyone!
I like the bold concepts you have uploaded. I would also like to see more simple ideas, using the light blue and dark grey used in the logo rather than black.
I would also like to see a few concepts that are a bit more feminine. Not overtly so but subtle.
Thank you!
I am unable to upload my logo at this time -- I will do this on Saturday evening when I get back in town.

```html
<!DOCTYPE html>
<html lang="en">
<head>
<meta charset="utf-8">
<title>trueLeaf Guidance – Business Card</title>
<link href="https://fonts.googleapis.com/css2?family=Open+Sans:wght@400;600;700&display=swap" rel="stylesheet">
<style>
  :root{
    --bg:#ececec;
    --card:#ffffff;
    --ink:#3b3d40;
    --band:#3a3b3d;
    --accent:#5fb3de;
    --muted:#55585c;
  }
  *{margin:0;padding:0;box-sizing:border-box}
  html,body{width:1200px;height:914px;overflow:hidden;background:var(--bg)}
  body{font-family:"Open Sans",Arial,sans-serif;position:relative}
  .card{
    position:absolute;left:100px;top:157px;width:1000px;height:600px;
    background:var(--card);box-shadow:0 4px 18px rgba(0,0,0,.12);
  }
  .brand{position:absolute;left:0;right:0;top:80px;text-align:center}
  .brand-mark{width:44px;height:44px;background:var(--accent);margin:0 auto 14px;border-radius:4px}
  .brand-name{font-size:52px;font-weight:700;color:var(--ink);letter-spacing:-.5px;line-height:1}
  .band-rule{position:absolute;left:0;width:100%;height:3px;background:var(--accent)}
  .band-rule.top{top:318px}
  .band-rule.bottom{top:394px}
  .band{
    position:absolute;left:0;top:326px;width:100%;height:63px;background:var(--band);
    display:flex;align-items:center;padding-left:66px;color:#fff;font-size:23px;font-weight:600;
  }
  .band .role{font-weight:400;margin-left:10px}
  .band .sep{margin-left:10px;font-weight:400}
  .contacts{position:absolute;left:66px;top:425px;color:var(--muted);font-size:19px}
  .contact-row{display:flex;align-items:center;margin-bottom:10px}
  .contact-item{display:flex;align-items:center;margin-right:22px}
  .icon{width:22px;height:22px;margin-right:8px;flex:none}
</style>
</head>
<body>
  <div class="card">
    <div class="brand">
      <div class="brand-mark"></div>
      <div class="brand-name">trueLeaf Guidance</div>
    </div>

    <div class="band-rule top"></div>
    <div class="band">
      <span class="name">Nora J. Halvers, MS, RD, LDN</span>
      <span class="sep">|</span>
      <span class="role">Registered Dietitian</span>
    </div>
    <div class="band-rule bottom"></div>

    <div class="contacts">
      <div class="contact-row">
        <span class="contact-item">
          <svg class="icon" viewBox="0 0 22 22" aria-hidden="true"><circle cx="11" cy="11" r="11" fill="var(--band)"/><path d="M11 4.5a4 4 0 0 0-4 4c0 3 4 8 4 8s4-5 4-8a4 4 0 0 0-4-4zm0 5.6a1.6 1.6 0 1 1 0-3.2 1.6 1.6 0 0 1 0 3.2z" fill="#fff"/></svg>
          418 West Meadow Lane Avon, Ohio 44011
        </span>
      </div>
      <div class="contact-row">
        <span class="contact-item">
          <svg class="icon" viewBox="0 0 22 22" aria-hidden="true"><circle cx="11" cy="11" r="11" fill="var(--band)"/><rect x="5" y="7" width="12" height="8" rx="1" fill="#fff"/><path d="M5.5 7.5 11 11.5l5.5-4" stroke="var(--band)" stroke-width="1.2" fill="none"/></svg>
          hello@trueleafguidance.com
        </span>
        <span class="contact-item">
          <svg class="icon" viewBox="0 0 22 22" aria-hidden="true"><circle cx="11" cy="11" r="11" fill="var(--band)"/><circle cx="11" cy="11" r="6" stroke="#fff" stroke-width="1.3" fill="none"/><ellipse cx="11" cy="11" rx="2.6" ry="6" stroke="#fff" stroke-width="1.1" fill="none"/><path d="M5 11h12" stroke="#fff" stroke-width="1.1"/></svg>
          www.trueleafguidance.com
        </span>
      </div>
    </div>
  </div>
</body>
</html>
```